National Female Non-profit Business Card

We need a business card design as soon as possible for a non-profit organisation called Meadow to Summit. Our aim is to empower leadership potential in rural female teens.
The business card should have our logo on the one side and then information on the other side, including name, job title, email address, phone number and website (www.meadowtosummit.com.au) and our twitter handle @MeadowSummit
It should use the colours white, coral (#f04a50) and orange (#f68e4e). The font used in the logo is Raleway.
The hashtag #YoungVoicesRise could be used.
It should be bright, chic and crisp. Our logo is attached.

Target Market(s)
We will be handing the cards out to politicians and senior executives. However, as we're a non-profit for young women, they also need to reflect femininity and youth.
Industry/Entity Type
Non-Profit

```html
<!DOCTYPE html>
<html lang="en">
<head>
<meta charset="utf-8">
<title>Meadow to Summit – Business Card</title>
<link rel="stylesheet" href="https://fonts.googleapis.com/css2?family=Open+Sans:wght@400;600&display=swap">
<style>
  :root {
    --coral: #f04a50;
    --orange: #f68e4e;
    --white: #ffffff;
    --ink: #3d3d3d;
    --stage: #eceef0;
  }
  * { box-sizing: border-box; margin: 0; padding: 0; }
  html, body { width: 1200px; height: 600px; overflow: hidden; }
  body {
    background: var(--stage);
    font-family: "Open Sans", sans-serif;
    position: relative;
  }
  .card {
    position: absolute;
    top: 152px;
    width: 467px;
    height: 278px;
    overflow: hidden;
  }
  .card-front {
    left: 93px;
    background: var(--coral);
    color: var(--white);
    text-align: center;
  }
  .card-front .brand-name {
    position: absolute;
    left: 0; right: 0;
    top: 164px;
    font-size: 24px;
    font-weight: 400;
    letter-spacing: 0.2px;
    text-transform: uppercase;
  }
  .card-front .website {
    position: absolute;
    left: 0; right: 0;
    top: 233px;
    font-size: 12px;
  }
  .card-back {
    left: 638px;
    background: var(--white);
  }
  .card-back .brand-name {
    position: absolute;
    left: 20px;
    top: 100px;
    font-size: 17px;
    color: var(--coral);
    text-transform: uppercase;
  }
  .contact-list {
    position: absolute;
    left: 24px;
    top: 140px;
    list-style: none;
    font-size: 11.5px;
    color: var(--ink);
    line-height: 15.8px;
  }
  .contact-list li { display: flex; align-items: flex-start; }
  .contact-list .icon {
    width: 11px; height: 11px;
    margin-right: 6px;
    margin-top: 2px;
    flex: none;
  }
  .contact-list .twitter { color: var(--coral); margin-top: 2px; }
  .divider {
    position: absolute;
    left: 258px;
    top: 142px;
    width: 1.5px;
    height: 94px;
    background: var(--coral);
  }
  .person {
    position: absolute;
    left: 315px;
    top: 150px;
  }
  .person .name { font-size: 14.5px; color: var(--coral); line-height: 16px; }
  .person .role { font-size: 10.5px; color: var(--orange); line-height: 12px; }
  .hashtag-band {
    position: absolute;
    left: 0; bottom: 10px;
    width: 467px; height: 18px;
  }
  .hashtag-band .hashtag {
    position: absolute;
    left: 20px; top: 1px;
    font-size: 11.5px;
    color: var(--white);
  }
</style>
</head>
<body>
  <section class="card card-front">
    <div class="brand-name">Meadow to Summit</div>
    <div class="website">www.meadowtosummit.com.au</div>
  </section>

  <section class="card card-back">
    <div class="brand-name">Meadow to Summit</div>

    <ul class="contact-list">
      <li>
        <svg class="icon" viewBox="0 0 12 12"><path d="M6 1 L11.5 6 H10 V11 H7.2 V7.8 H4.8 V11 H2 V6 H0.5 Z" fill="var(--coral)"/></svg>
        <span>4820 1/2 Willow rd Ashford<br>TX, 77470</span>
      </li>
      <li>
        <svg class="icon" viewBox="0 0 12 12"><path d="M1 4 Q6 0 11 4 L9.5 5.5 L8 4.5 V3.8 Q6 3 4 3.8 V4.5 L2.5 5.5 Z M2.5 6.5 H9.5 L10.5 11 H1.5 Z" fill="var(--coral)"/></svg>
        <span>03 5550 1287</span>
      </li>
      <li>
        <svg class="icon" viewBox="0 0 12 12"><rect x="0.5" y="2" width="11" height="8" fill="var(--coral)"/><path d="M1 2.5 L6 6.5 L11 2.5" stroke="#fff" stroke-width="1" fill="none"/></svg>
        <span>hello@meadowtosummit.com.au</span>
      </li>
      <li>
        <svg class="icon" viewBox="0 0 12 12"><circle cx="6" cy="6" r="5" fill="none" stroke="var(--coral)" stroke-width="1.4"/><path d="M1 6 H11 M6 1 Q3 6 6 11 M6 1 Q9 6 6 11" stroke="var(--coral)" stroke-width="1" fill="none"/></svg>
        <span>www.meadowtosummit.com.au</span>
      </li>
      <li>
        <svg class="icon twitter" viewBox="0 0 12 12"><circle cx="6" cy="6" r="5" fill="var(--coral)"/></svg>
        <span class="twitter">@MeadowSummit</span>
      </li>
    </ul>

    <div class="divider"></div>

    <div class="person">
      <div class="name">Amelia Brooks</div>
      <div class="role">Manager</div>
    </div>

    <div class="hashtag-band">
      <svg width="467" height="18" viewBox="0 0 467 18">
        <polygon points="0,0 310,0 302,18 0,18" fill="var(--coral)"/>
        <polygon points="314,0 467,0 467,18 306,18" fill="var(--orange)"/>
      </svg>
      <span class="hashtag">#YoungVoicesRise</span>
    </div>
  </section>
</body>
</html>
```